Business Card Design

I need a business card for my corporation. We are a fast food Mexican Taqueria located in San Jose, CA. I want the cards to include our business logo. The cards need to be simple but elegant. Our theme through out our locations is a beach feel atmosphere. I would like to see cards with a beach feeling. Our website is tacosdelpuerto.net and it would be great if the cards matched our website.

Industry/Entity Type

Business

Contact Information for Business Card

Monica Ferrer, VP
2637 Birch Hollow Ave
Mar Vista Bay, CA 90000
Direct: 7605527319

```html
<!DOCTYPE html>
<html lang="en">
<head>
<meta charset="utf-8">
<title>Del Puerto Business Card</title>
<link rel="stylesheet" href="https://fonts.googleapis.com/css2?family=Cinzel:wght@400;600&display=swap">
<style>
  :root {
    --bg: #e4e3e1;
    --card: #f7f7f6;
    --red: #c2202b;
    --yellow: #f0d20f;
    --stripe: #e4e4e4;
    --shadow: rgba(0,0,0,0.18);
  }
  * { margin: 0; padding: 0; box-sizing: border-box; }
  html, body { width: 1200px; height: 864px; overflow: hidden; }
  body {
    background: var(--bg);
    font-family: "Cinzel", serif;
    position: relative;
  }
  .card {
    position: absolute;
    width: 540px;
    height: 309px;
    background: var(--card);
    box-shadow: 0 6px 18px var(--shadow);
    overflow: hidden;
  }
  .card-back { left: 620px; top: 120px; }
  .card-front { left: 40px; top: 430px; }
  .card svg.bands { position: absolute; inset: 0; }

  .brand {
    position: absolute;
    display: flex;
    align-items: center;
    gap: 10px;
    color: var(--red);
    font-weight: 600;
    white-space: nowrap;
  }
  .brand-sun {
    border-radius: 50%;
    background: var(--yellow);
    flex: none;
  }
  .card-back .brand { left: 150px; top: 105px; font-size: 42px; }
  .card-back .brand-sun { width: 30px; height: 30px; }
  .card-front .brand { left: 34px; top: 30px; font-size: 30px; }
  .card-front .brand-sun { width: 22px; height: 22px; }

  .person-name {
    position: absolute;
    right: 30px; top: 92px;
    color: var(--red);
    font-size: 18px;
    letter-spacing: 3px;
    white-space: nowrap;
  }
  .address {
    position: absolute;
    left: 74px; top: 138px;
    color: var(--red);
    font-size: 12px;
    letter-spacing: 0.5px;
    white-space: nowrap;
  }
  .phone {
    position: absolute;
    left: 74px; top: 176px;
    color: var(--red);
    font-size: 20px;
    letter-spacing: 1px;
    white-space: nowrap;
  }
  .icon {
    position: absolute;
    left: 30px;
    width: 26px; height: 26px;
  }
  .icon-pin { top: 132px; }
  .icon-phone { top: 174px; }
</style>
</head>
<body>

<section class="card card-back">
  <svg class="bands" width="540" height="309" viewBox="0 0 540 309">
    <polygon points="0,190 290,190 300,204 0,204" fill="var(--red)"/>
    <polygon points="296,204 540,204 540,218 306,218" fill="var(--yellow)"/>
  </svg>
  <div class="brand"><span class="brand-sun"></span>Del Puerto</div>
</section>

<section class="card card-front">
  <svg class="bands" width="540" height="309" viewBox="0 0 540 309">
    <rect x="0" y="124" width="540" height="36" fill="var(--stripe)"/>
    <rect x="0" y="160" width="540" height="149" fill="var(--yellow)"/>
    <path d="M0,222 L300,232 C350,234 362,206 420,204 L540,204 L540,309 L0,309 Z" fill="var(--red)"/>
  </svg>

  <div class="brand"><span class="brand-sun"></span>Del Puerto</div>
  <div class="person-name">Monica Ferrer</div>

  <svg class="icon icon-pin" viewBox="0 0 28 28" aria-label="Address">
    <rect width="28" height="28" rx="5" fill="var(--red)"/>
    <path d="M14 6a6 6 0 0 0-6 6c0 4.5 6 10 6 10s6-5.5 6-10a6 6 0 0 0-6-6z" fill="var(--yellow)"/>
    <circle cx="14" cy="12" r="2.2" fill="var(--red)"/>
  </svg>
  <div class="address">VP 2637 Birch Hollow Ave Mar Vista Bay, CA 90000</div>

  <svg class="icon icon-phone" viewBox="0 0 28 28" aria-label="Phone">
    <rect width="28" height="28" rx="5" fill="var(--red)"/>
    <path d="M7 11c0-2 3-3 7-3s7 1 7 3v1.5h-3.5V11h-7v1.5H7z" fill="var(--yellow)"/>
    <rect x="9" y="13" width="10" height="8" rx="1.5" fill="var(--yellow)"/>
    <circle cx="14" cy="17" r="2" fill="var(--red)"/>
  </svg>
  <div class="phone">7605527319</div>
</section>

</body>
</html>
```